Trovadel Ltda

Logo design focused on: - Construction of civil works - Electrical services - Metal structures - Equipment rental Tomas Ibarra Luque Manager trovadel.ltda@norvexmail.com 56 9 41827035 Quirobamba s / n, Tolvas, San Pedro de Arenal

Target Market(s)

Building

Colors
33a6d7
0292cd
33b8a4
0555a3

```html
<!DOCTYPE html>
<html lang="es">
<head>
<meta charset="utf-8">
<title>Trovadel Ltda — Tarjetas de presentación</title>
<link href="https://fonts.googleapis.com/css2?family=Open+Sans:wght@400;600&display=swap" rel="stylesheet">
<style>
  :root{
    --bg:#3a3a3c;
    --front-start:#2f82c8;
    --front-end:#14bcc6;
    --back-start:#2a313b;
    --back-end:#131a23;
    --white:#ffffff;
    --accent-blue:#0555a3;
    --sky:#33a6d7;
    --teal:#33b8a4;
    --ink-light:#b9c0c8;
  }
  *{box-sizing:border-box;margin:0;padding:0}
  html,body{width:1200px;height:900px;overflow:hidden}
  body{background:var(--bg);font-family:"Open Sans",sans-serif;position:relative}
  .card{position:absolute;left:270px;width:660px;height:377px;border-radius:22px;overflow:hidden;box-shadow:0 10px 30px rgba(0,0,0,.45)}
  .card--front{top:52px;background:linear-gradient(135deg,var(--front-start),var(--front-end))}
  .card--back{top:472px;background:linear-gradient(135deg,var(--back-start),var(--back-end))}

  .services{position:absolute;left:48px;top:150px;list-style:none;color:var(--white);font-size:18px;line-height:33px}
  .services li::before{content:"";display:inline-block;width:8px;height:8px;border-radius:50%;background:var(--white);margin-right:8px;vertical-align:middle}

  .brand{position:absolute;display:flex;align-items:center;gap:12px}
  .brand__dot{width:52px;height:52px;border-radius:50%;flex:none}
  .brand__name{font-size:24px;font-weight:400;letter-spacing:1px;white-space:nowrap}
  .card--front .brand{left:362px;top:110px}
  .card--front .brand__dot{background:var(--white)}
  .card--front .brand__name{color:var(--white)}
  .card--back .brand{left:48px;top:250px}
  .card--back .brand__dot{background:var(--sky)}
  .card--back .brand__name{color:var(--sky)}

  .divider{position:absolute;left:336px;top:70px;width:2px;height:230px;background:var(--accent-blue)}
  .contact{position:absolute;left:362px;top:78px;color:var(--ink-light)}
  .contact__name{font-size:24px;color:#c9ced4;letter-spacing:-.5px}
  .contact__role{font-size:16px;color:var(--sky);margin-bottom:16px}
  .contact__row{display:flex;align-items:flex-start;gap:10px;font-size:15px;line-height:21px;margin-bottom:10px}
  .contact__row svg{flex:none;margin-top:3px}
</style>
</head>
<body>
  <section class="card card--front" aria-label="Anverso">
    <ul class="services">
      <li>Construcción de Obras Civiles</li>
      <li>Servicios eléctricos</li>
      <li>Estructuras metálicas</li>
      <li>Arriendo de Equipos</li>
    </ul>
    <div class="brand">
      <span class="brand__dot"></span>
      <span class="brand__name">TROVADEL Ltda</span>
    </div>
  </section>

  <section class="card card--back" aria-label="Reverso">
    <div class="brand">
      <span class="brand__dot"></span>
      <span class="brand__name">TROVADEL Ltda</span>
    </div>
    <span class="divider"></span>
    <div class="contact">
      <p class="contact__name">Tomas Ibarra Luque</p>
      <p class="contact__role">Gerente</p>
      <p class="contact__row">
        <svg width="18" height="14" viewBox="0 0 18 14"><rect x="1" y="1" width="16" height="12" fill="var(--sky)"/><path d="M1 1l8 7 8-7" fill="none" stroke="#131a23" stroke-width="1.5"/></svg>
        trovadel.ltda@norvexmail.com
      </p>
      <p class="contact__row">
        <svg width="18" height="16" viewBox="0 0 18 16"><path d="M2 6c0-3 3-4 7-4s7 1 7 4l-3 1-1-2H6L5 7z" fill="var(--sky)"/><rect x="3" y="8" width="12" height="7" rx="1.5" fill="var(--sky)"/></svg>
        +56 9 41827035
      </p>
      <p class="contact__row">
        <svg width="18" height="20" viewBox="0 0 16 20"><path d="M8 1a6 6 0 0 1 6 6c0 5-6 12-6 12S2 12 2 7a6 6 0 0 1 6-6z" fill="var(--sky)"/><circle cx="8" cy="7" r="2.3" fill="#131a23"/></svg>
        <span>Quirobamba s/n, Tolvas<br>San Pedro de Arenal</span>
      </p>
    </div>
  </section>
</body>
</html>
```